Website design for a Recruitment Agency in the Pacific Islands

Website for jobseekers to search for work, employers to list vacancies and also for workers to upload their resumes for possible job prospects.

The website will be called ' Korowai Staffing' and this needs to reflect the Pacific Islanders searching for jobs or working in the fields.
Must be connected to a database that collects details for workers which can be downloaded onto an excel spreadsheet for quick reviews offline
The website must also have an app for ios and android so this can be easily downloaded for individuals who want to do quick job searches without going onto the website.

The main objective of this website is to list job opportunities in all Pacific Island Countries or even overseas which Pacific Islanders can apply.

The theme of fishing means ' there is alot of fish in the sea ' = lots of workers in the Pacific Ocean.

Target Market(s)

Agriculture, Fisheries, constructions and mining

Industry/Entity Type

Agriculture, Constructions and Fisheries

Font styles to use
Other font styles liked:
• Muli

Colors
E54698
E96AAD
F1A4CE
F9D9EA
FCEFF6

Requirements
Must have
• Must have an App, adroid and ios
Nice to have
• - pictures of Pacific Islanders , pictures of Pacific Islanders at work in mines, in fisheries and in agricultures

```html
<!DOCTYPE html>
<html lang="en">
<head>
<meta charset="utf-8">
<title>Korowai Staffing – Recruitment across the Pacific</title>
<link href="https://fonts.googleapis.com/css2?family=Mulish:wght@300;400;500;600;700;800&display=swap" rel="stylesheet">
<style>
:root{
  --pink:#e54698;
  --pink-2:#e96aad;
  --pink-3:#f1a4ce;
  --pink-4:#f9d9ea;
  --pink-5:#fceff6;
  --ink:#1d1d1f;
  --text:#555;
  --muted:#888;
  --dark:#141414;
  --plum:#3a1628;
  --white:#fff;
  --card-shadow:0 4px 18px rgba(0,0,0,.09);
}
*{box-sizing:border-box;margin:0;padding:0}
html,body{width:1200px;height:4950px;overflow:hidden}
body{position:relative;font-family:'Mulish',sans-serif;color:var(--ink);background:var(--white)}
.abs{position:absolute}
.section{position:absolute;left:0;width:1200px}
.section-title{position:absolute;left:0;width:1200px;text-align:center;font-weight:500;font-size:38px;letter-spacing:.2px}

/* top bar */
.topbar{top:0;height:23px;background:var(--pink);color:var(--white);font-size:11px}
.topbar .call{position:absolute;right:124px;top:5px}

/* hero */
.hero{top:23px;height:580px;background:linear-gradient(100deg,#1a1210 0%,#3a2418 40%,#5a3a22 58%,#2a1a12 80%,#120c0a 100%);overflow:hidden}
.hero .brand{position:absolute;left:70px;top:38px;color:var(--pink);font-size:12px;font-weight:700;display:flex;align-items:center;gap:6px}
.hero .brand i{display:block;width:26px;height:26px;border-radius:50%;border:2px solid var(--pink)}
.nav{position:absolute;top:20px;right:70px;display:flex;align-items:center;gap:0;font-size:12px;color:var(--white);letter-spacing:.2px}
.nav a{color:var(--white);text-decoration:none;padding:14px 14px}
.nav a.active{background:var(--pink)}
.nav .search{width:24px;height:24px;border-radius:50%;border:1px solid rgba(255,255,255,.6);margin-left:10px;position:relative}
.nav .search:after{content:"";position:absolute;left:6px;top:6px;width:8px;height:8px;border:1.5px solid #fff;border-radius:50%}
.hero h1{position:absolute;left:70px;top:180px;color:var(--white);font-weight:400;font-size:36px;line-height:1.2}
.hero h1 b{display:block;font-weight:800;font-size:42px}
.hero .lead{position:absolute;left:70px;top:284px;color:var(--white);font-size:14px}
.hero .btns{position:absolute;left:70px;top:324px;display:flex;gap:14px}
.btn{display:inline-block;font-size:11px;padding:12px 12px;font-family:inherit;border:0}
.btn-pink{background:var(--pink);color:var(--white)}
.btn-white{background:var(--white);color:var(--ink);padding:12px 22px}
.btn-dark{background:var(--dark);color:var(--white)}
.hero .arrow{position:absolute;top:270px;width:22px;height:22px;border-left:2px solid #fff;border-bottom:2px solid #fff}
.hero .arrow.prev{left:22px;transform:rotate(45deg)}
.hero .arrow.next{right:22px;transform:rotate(-135deg)}
.hero svg.wave{position:absolute;left:0;bottom:0}

/* job cards */
.jobs{top:640px;height:880px}
.jobs .section-title{top:10px}
.job-card{position:absolute;width:337px;height:361px;background:var(--white);box-shadow:var(--card-shadow);padding:28px 30px}
.job-card .logo{width:56px;height:56px;border-radius:6px}
.job-card h3{font-weight:500;font-size:17px;margin-top:22px}
.job-card p{font-size:12.5px;line-height:19px;color:var(--text);margin-top:14px}
.tags{display:flex;gap:8px;margin-top:14px}
.tags span{background:#ececec;font-size:10px;color:#444;padding:7px 14px;border-radius:3px}
.job-card .actions{display:flex;gap:4px;margin-top:30px}
.job-card .actions .btn{width:128px;text-align:center}

/* services */
.services{top:1530px;height:580px;background:transparent}
.services .bg{position:absolute;left:0;top:0}
.services .eyebrow{position:absolute;top:100px;width:1200px;text-align:center;color:#ddd;font-size:17px}
.services .section-title{top:122px;color:var(--white)}
.service{position:absolute;top:187px;width:248px;text-align:center;color:var(--white)}
.service .photo{height:212px;border-radius:10px}
.service .badge{width:34px;height:34px;border-radius:50%;background:var(--pink);margin:-18px auto 0;border:3px solid rgba(255,255,255,.25);position:relative}
.service h4{font-weight:500;font-size:17px;margin-top:8px;line-height:23px}
.service p{font-size:12.5px;color:#ccc;line-height:19px;margin-top:4px;padding:0 14px}

/* app */
.app{top:2100px;height:490px}
.app .phones{position:absolute;left:232px;top:44px;width:364px;height:446px;border-radius:26px;background:linear-gradient(160deg,#d9d9dc,#8a8a8f 40%,#2b2b30 70%,#c8c8cc)}
.app h2{position:absolute;left:700px;top:160px;font-weight:600;font-size:36px}
.app p{position:absolute;left:700px;top:230px;width:430px;font-size:13px;line-height:22px;color:var(--text)}
.store{position:absolute;top:319px;width:138px;height:44px;border-radius:6px;background:#000;border:1px solid #999}

/* training */
.training{top:2588px;height:440px}
.training .bg{position:absolute;left:0;top:0}
.training .section-title{top:44px;color:var(--white)}
.course{position:absolute;top:116px;width:248px;text-align:center;color:var(--white)}
.course .photo{height:176px}
.course h4{font-weight:600;font-size:16px;margin-top:26px}

/* testimonials */
.testimonials{top:3080px;height:360px}
.testimonials .section-title{top:16px}
.quote{position:absolute;top:87px;width:337px;height:237px;background:#f1f7fb;padding:20px 18px}
.quote .mark{font-size:34px;line-height:20px;color:#999;font-weight:800;font-family:Georgia,serif}
.quote p{font-size:13px;line-height:22px;color:var(--text);margin-top:12px}
.quote h5{font-weight:500;font-size:15px;margin-top:20px}
.quote small{display:block;font-size:10px;color:var(--muted)}
.quote .avatar{position:absolute;right:20px;bottom:-18px;width:48px;height:48px;border-radius:50%;border:3px solid var(--pink);background:#c9b3a5}

/* contact */
.contact{top:3440px;height:490px}
.contact .bg{position:absolute;left:0;top:0}
.contact h2{position:absolute;top:100px;width:1200px;text-align:center;color:var(--white);font-weight:500;font-size:38px}
.contact .sub{position:absolute;top:153px;width:1200px;text-align:center;color:#ddd;font-size:14px}
.field{position:absolute;color:#ddd;font-size:11px;border-bottom:1px solid #888;padding-bottom:10px}
.contact .send{position:absolute;left:537px;top:417px;width:126px;text-align:center}

/* about */
.about{top:3930px;height:560px}
.about .art{position:absolute;left:110px;top:30px;width:420px;height:440px;border-radius:50%;background:radial-gradient(circle at 55% 55%,#e4f0d2 0%,#f5f2ea 45%,#fff 70%)}
.about .eyebrow{position:absolute;left:611px;top:156px;font-size:17px}
.about h2{position:absolute;left:611px;top:188px;font-weight:600;font-size:36px}
.about p{position:absolute;left:611px;top:254px;width:520px;font-size:13px;line-height:22px;color:var(--text)}
.about .more{position:absolute;left:611px;top:396px;width:132px;text-align:center;letter-spacing:1px;font-size:10px;padding:14px 0}

/* footer */
.footer{top:4440px;height:510px;color:#ddd}
.footer .bg{position:absolute;left:0;top:0}
.footer .brand{position:absolute;left:77px;top:150px;font-size:15px;color:var(--white);font-weight:600;display:flex;align-items:center;gap:8px}
.footer .brand i{width:22px;height:22px;border-radius:50%;border:1.5px solid #fff;display:block}
.socials{position:absolute;left:72px;top:335px;display:flex;gap:8px}
.socials span{width:30px;height:30px;border-radius:50%;background:#2a2a2a;display:block}
.fcol{position:absolute;top:150px;font-size:12px}
.fcol h6{color:var(--pink);font-weight:500;font-size:18px;margin-bottom:14px}
.fcol li{list-style:none;line-height:27px;color:var(--white)}
.contact-row{display:flex;gap:10px;align-items:flex-start;margin-bottom:22px;line-height:15px;color:var(--white)}
.contact-row svg{flex:none}
.copyright{position:absolute;top:440px;width:1200px;text-align:center;font-size:12px;color:#bbb}
.copyright b{color:var(--white);font-weight:500}
</style>
</head>
<body>

<div class="section topbar"><span class="call">&#9742; Call: 0400 518 274</span></div>

<header class="section hero">
  <div role="img" aria-label="Photo of miners with helmet lamps working underground" class="abs" style="inset:0"></div>
  <div class="brand"><i></i>Korowai Staffing</div>
  <nav class="nav">
    <a class="active">HOME</a><a>ABOUT US</a><a>SERVICES</a><a>JOB SEEKER</a><a>PORTAL</a><a>TRAINING INFO</a><a>CONTACT US</a><span class="search"></span>
  </nav>
  <span class="arrow prev"></span><span class="arrow next"></span>
  <h1>Find the<b>Perfect Job for you</b></h1>
  <div class="lead">Search your career opportunity through 12,800 jobs</div>
  <div class="btns"><span class="btn btn-pink">I am looking for a Job</span><span class="btn btn-white">I am an Employer</span></div>
  <svg class="wave" width="1200" height="220" viewBox="0 0 1200 220"><path d="M0,100 C260,150 460,230 700,180 C900,140 1060,40 1200,20 L1200,220 L0,220Z" fill="#fff"/></svg>
</header>

<section class="section jobs">
  <h2 class="section-title">Job Seekers</h2>
  <article class="job-card" style="left:71px;top:85px"><div class="logo" style="background:#4b2b3e"></div><h3>Finibus Bonorum</h3><p>Sed ut perspiciatis unde omnis iste natus error sit voluptatem accusantium doloremque laudantium totam rem aperiam, eaque ipsa quae ab illo inventore...</p><div class="tags"><span>Full Time</span><span>Min 1 Year</span><span>Senior Level</span></div><div class="actions"><span class="btn btn-pink">Apply Now</span><span class="btn btn-dark">Message</span></div></article>
  <article class="job-card" style="left:431px;top:85px"><div class="logo" style="background:#b65a8a"></div><h3>Finibus Bonorum</h3><p>Sed ut perspiciatis unde omnis iste natus error sit voluptatem accusantium doloremque laudantium totam rem aperiam, eaque ipsa quae ab illo inventore...</p><div class="tags"><span>Full Time</span><span>Min 1 Year</span><span>Senior Level</span></div><div class="actions"><span class="btn btn-pink">Apply Now</span><span class="btn btn-dark">Message</span></div></article>
  <article class="job-card" style="left:791px;top:85px"><div class="logo" style="background:#4c7d98"></div><h3>Finibus Bonorum</h3><p>Sed ut perspiciatis unde omnis iste natus error sit voluptatem accusantium doloremque laudantium totam rem aperiam, eaque ipsa quae ab illo inventore...</p><div class="tags"><span>Full Time</span><span>Min 1 Year</span><span>Senior Level</span></div><div class="actions"><span class="btn btn-pink">Apply Now</span><span class="btn btn-dark">Message</span></div></article>
  <article class="job-card" style="left:71px;top:471px"><div class="logo" style="background:#e46d1f"></div><h3>Finibus Bonorum</h3><p>Sed ut perspiciatis unde omnis iste natus error sit voluptatem accusantium doloremque laudantium totam rem aperiam, eaque ipsa quae ab illo inventore...</p><div class="tags"><span>Full Time</span><span>Min 1 Year</span><span>Senior Level</span></div><div class="actions"><span class="btn btn-pink">Apply Now</span><span class="btn btn-dark">Message</span></div></article>
  <article class="job-card" style="left:431px;top:471px"><div class="logo" style="background:#1d4d6e"></div><h3>Finibus Bonorum</h3><p>Sed ut perspiciatis unde omnis iste natus error sit voluptatem accusantium doloremque laudantium totam rem aperiam, eaque ipsa quae ab illo inventore...</p><div class="tags"><span>Full Time</span><span>Min 1 Year</span><span>Senior Level</span></div><div class="actions"><span class="btn btn-pink">Apply Now</span><span class="btn btn-dark">Message</span></div></article>
  <article class="job-card" style="left:791px;top:471px"><div class="logo" style="background:#3f8a5c"></div><h3>Finibus Bonorum</h3><p>Sed ut perspiciatis unde omnis iste natus error sit voluptatem accusantium doloremque laudantium totam rem aperiam, eaque ipsa quae ab illo inventore...</p><div class="tags"><span>Full Time</span><span>Min 1 Year</span><span>Senior Level</span></div><div class="actions"><span class="btn btn-pink">Apply Now</span><span class="btn btn-dark">Message</span></div></article>
</section>

<section class="section services">
  <svg class="bg" width="1200" height="580" viewBox="0 0 1200 580"><defs><linearGradient id="svcbg" x1="0" y1="0" x2="0" y2="1"><stop offset="0" stop-color="#2a2a2a"/><stop offset="1" stop-color="#121212"/></linearGradient></defs><path d="M0,36 C220,60 420,70 640,36 C820,8 980,-6 1200,22 L1200,580 L0,580Z" fill="url(#svcbg)"/></svg>
  <div class="eyebrow">Our Services</div>
  <h2 class="section-title">What We Offer Assistance</h2>
  <div class="service" style="left:71px"><div class="photo" role="img" aria-label="Photo of candidates waiting for a job interview" style="background:linear-gradient(135deg,#d9dde2,#8f969e)"></div><div class="badge"></div><h4>Recruitment<br>Process Outsourced</h4><p>Sed ut perspiciatis unde omnis iste natus error</p></div>
  <div class="service" style="left:341px"><div class="photo" role="img" aria-label="Photo of a handshake across a meeting table" style="background:linear-gradient(135deg,#e6dccd,#9ba6b0)"></div><div class="badge"></div><h4>Temporary Hire</h4><p>Sed ut perspiciatis unde omnis iste natus error</p></div>
  <div class="service" style="left:611px"><div class="photo" role="img" aria-label="Photo of a smiling professional in a jacket" style="background:linear-gradient(135deg,#eef0ee,#b8b2a8)"></div><div class="badge"></div><h4>Permanent Hire</h4><p>Sed ut perspiciatis unde omnis iste natus error</p></div>
  <div class="service" style="left:881px"><div class="photo" role="img" aria-label="Photo of a cheerful worker holding a folder" style="background:linear-gradient(135deg,#f1f1f1,#e2b860)"></div><div class="badge"></div><h4>Managed Services</h4><p>Sed ut perspiciatis unde omnis iste natus error</p></div>
</section>

<section class="section app">
  <div class="phones" role="img" aria-label="Two smartphones showing the mobile app"></div>
  <h2>Get A Mobile App</h2>
  <p>Sed ut perspiciatis unde omnis iste natus error sit voluptatem accusantium doloremque laudantium, totam rem aperiam, eaque ipsa quae ab illo inventore veritatis...</p>
  <span class="store" style="left:700px" role="img" aria-label="Android store download badge"></span>
  <span class="store" style="left:846px" role="img" aria-label="iOS store download badge"></span>
</section>

<section class="section training">
  <svg class="bg" width="1200" height="440" viewBox="0 0 1200 440"><path d="M0,0 L1200,0 L1200,400 C960,390 760,420 560,432 C360,444 160,420 0,410Z" fill="#1b1b1b"/></svg>
  <h2 class="section-title">Training</h2>
  <div class="course" style="left:71px"><div class="photo" role="img" aria-label="Photo of a first aid class practising CPR" style="background:linear-gradient(135deg,#c9b8a8,#6d5a4b)"></div><h4>Firstaid</h4></div>
  <div class="course" style="left:341px"><div class="photo" role="img" aria-label="Photo of a worker with a tablet in a green field" style="background:linear-gradient(180deg,#cfe0c6,#5a7d3e)"></div><h4>Health &amp; Hygene</h4></div>
  <div class="course" style="left:611px"><div class="photo" role="img" aria-label="Photo of workers tending plants in a greenhouse" style="background:linear-gradient(180deg,#d8ddd5,#5f7a4b)"></div><h4>Manual Handeling</h4></div>
  <div class="course" style="left:881px"><div class="photo" role="img" aria-label="Photo of a hand holding a young plant" style="background:radial-gradient(circle at 50% 60%,#c6df56,#3d6a1b)"></div><h4>Worlplace Health &amp; Safety</h4></div>
</section>

<section class="section testimonials">
  <h2 class="section-title">Testimonials</h2>
  <blockquote class="quote" style="left:71px"><div class="mark">&ldquo;</div><p>Sed ut perspiciatis unde omnis iste natus error sit voluptatem accusantium doloremque laudantium, totam rem aperiam, eaque ipsa quae ab illo inventore veritatis et quasi architecto beatae vitae dicta sunt explicabo.</p><h5>Lani Tupou</h5><small>Agriculture</small><span class="avatar" role="img" aria-label="Portrait photo"></span></blockquote>
  <blockquote class="quote" style="left:431px"><div class="mark">&ldquo;</div><p>Sed ut perspiciatis unde omnis iste natus error sit voluptatem accusantium doloremque laudantium, totam rem aperiam, eaque ipsa quae ab illo inventore veritatis et quasi architecto beatae vitae dicta sunt explicabo.</p><h5>Sione Kaufana</h5><small>Management</small><span class="avatar" role="img" aria-label="Portrait photo"></span></blockquote>
  <blockquote class="quote" style="left:791px"><div class="mark">&ldquo;</div><p>Sed ut perspiciatis unde omnis iste natus error sit voluptatem accusantium doloremque laudantium, totam rem aperiam, eaque ipsa quae ab illo inventore veritatis et quasi architecto beatae vitae dicta sunt explicabo.</p><h5>Mere Naidu</h5><small>Agriculture</small><span class="avatar" role="img" aria-label="Portrait photo"></span></blockquote>
</section>

<section class="section contact">
  <svg class="bg" width="1200" height="490" viewBox="0 0 1200 490"><defs><linearGradient id="ctbg" x1="0" y1="0" x2="0" y2="1"><stop offset="0" stop-color="#3b1a2c"/><stop offset="1" stop-color="#2a1220"/></linearGradient></defs><path d="M0,40 C180,10 360,60 560,50 C780,38 960,-10 1200,20 L1200,490 L0,490Z" fill="url(#ctbg)"/></svg>
  <h2>Contact Us</h2>
  <div class="sub">Sed ut perspiciatis unde omnis iste natus error sit voluptatem accusantium</div>
  <div class="field" style="left:271px;top:210px;width:318px">Name:</div>
  <div class="field" style="left:608px;top:210px;width:321px">Phone:</div>
  <div class="field" style="left:271px;top:262px;width:658px">Email:</div>
  <div class="field" style="left:271px;top:314px;width:658px;height:84px">Comments:</div>
  <span class="btn btn-pink send">Apply Now</span>
</section>

<section class="section about">
  <div class="art" role="img" aria-label="Illustration of a network of connected dots forming a sea creature"></div>
  <div class="eyebrow">Welcome To</div>
  <h2>Korowai Staffing</h2>
  <p>Korowai Staffing PTY LTD is a labour hire recruiting and logistical support service located, in both Papua New Guinea and Australia. With its headquarters located in Townsville QLD Australia, while also having an office base in Lae Papua New Guinea run by Tomas and his team with Reefline Logistics.</p>
  <span class="btn btn-pink more">READ MORE</span>
</section>

<footer class="section footer">
  <svg class="bg" width="1200" height="510" viewBox="0 0 1200 510"><path d="M0,110 C240,90 520,120 760,80 C960,46 1080,10 1200,0 L1200,510 L0,510Z" fill="#050505"/></svg>
  <div class="brand"><i></i>Korowai Staffing</div>
  <div class="socials"><span aria-label="Social link"></span><span aria-label="Social link"></span><span aria-label="Social link"></span></div>
  <div class="fcol" style="left:273px"><h6>Quick Links</h6><ul><li>Home</li><li>About Us</li><li>Services</li><li>Job Seeker</li><li>Portal</li><li>Training Info</li><li>Contact Us</li></ul></div>
  <div class="fcol" style="left:448px"><h6>Services</h6><ul><li>Recruitment Process Outsourced</li><li>Temporary Hire</li><li>Permanent Hire</li><li>Managed Services</li><li>Seasonal Work</li></ul></div>
  <div class="fcol" style="left:700px"><h6>Training</h6><ul><li>Firstaid</li><li>Health &amp; Hygene</li><li>Manual Handeling</li><li>Worplace Health &amp; Safety</li></ul></div>
  <div class="fcol" style="left:908px;width:240px"><h6>Contacts</h6>
    <div class="contact-row"><svg width="26" height="26" viewBox="0 0 26 26"><circle cx="13" cy="13" r="13" fill="#e54698"/><path d="M13 6a4.5 4.5 0 0 0-4.5 4.5c0 3.4 4.5 8.5 4.5 8.5s4.5-5.1 4.5-8.5A4.5 4.5 0 0 0 13 6zm0 6.2a1.7 1.7 0 1 1 0-3.4 1.7 1.7 0 0 1 0 3.4z" fill="#fff"/></svg><span>22/B Harbour Road, Lae and Brisbane.</span></div>
    <div class="contact-row"><svg width="26" height="26" viewBox="0 0 26 26"><circle cx="13" cy="13" r="13" fill="#e54698"/><path d="M9.5 7.5l2 2.6-1.2 1.4a8 8 0 0 0 4.2 4.2l1.4-1.2 2.6 2-1.2 1.8c-4.6-.4-8.8-4.6-9.2-9.2z" fill="#fff"/></svg><span style="padding-top:5px">0400 518 274</span></div>
    <div class="contact-row"><svg width="26" height="26" viewBox="0 0 26 26"><circle cx="13" cy="13" r="13" fill="#e54698"/><rect x="7.5" y="9" width="11" height="8" rx="1" fill="#fff"/><path d="M7.5 9.5l5.5 4 5.5-4" stroke="#e54698" stroke-width="1.2" fill="none"/></svg><span style="padding-top:5px">hello@korowai.example</span></div>
  </div>
  <div class="copyright">Copyright &copy; 2022 <b>Korowai Staffing</b>. All Rights Reserved.</div>
</footer>

</body>
</html>
```